Webdesign für einen Hersteller von hochpräzisen Durchflussmessern und Drucksensoren
Zielgruppe
Wir sind die KVR GmbH & Co. KG, ein deutscher Hersteller von hochpräzisen Durchflussmessern und Drucksensoren für industrielle Anwendungen. Unsere Produkte werden weltweit in Prüfständen, Automotive-Testing, Maschinenbau, Energie- und Prozessindustrie eingesetzt.
Unsere Zielgruppe sind technische Entscheider, Ingenieure, Entwicklungsleiter und Einkäufer in B2B-Unternehmen. Die Website dient als Produkt- und Markenpräsentation, Lead-Generierung sowie als Vertrauensbasis vor Kontaktaufnahme oder Angebotsanfrage.
Wichtig ist ein hochwertiger, technologischer, international verständlicher Auftritt, der Kompetenz, Präzision und Innovationskraft vermittelt.
Aufgabenstellung
Es existiert bereits ein Logo und Corporate Design, das beibehalten werden soll. Die neue Gestaltung des bestehenden Wordpress-Auftritts soll dieses modernisieren und konsistenter anwenden.
Designstil:
• Modern, clean, technisch, hochwertig
• Viel Weißraum, klare Typografie
• Präzise Linien, dezente technische Grafikelemente
Farben:
• Bestehende Markenfarben aus dem Logo beibehalten
• Hauptfarbe: Blau / Dunkelblau
• Ergänzend Grau- und Weißtöne
• Akzentfarben #d15c04 sparsam einsetzen
Bildsprache:
• Hochwertige Produktfotos
• Industrie- und Anwendungsszenen
• Detailaufnahmen von Sensoren / Technik
• Optional abstrakte technische Visuals oder Liniengrafiken
UX-Anforderungen:
• Klare Navigation für Produktbereiche
• Schneller Zugang zu Produktdetails
• Call-to-Action für Kontakt / Anfrage
• International verständliches Layout (englische Seite folgt später)
Technische Hinweise:
• Die Seite wird später in WordPress umgesetzt
• Responsive Design für Desktop / Tablet / Mobile
• SEO-freundliche Struktur
Design-Tool Präferenz:
• Figma bevorzugt

```html
<!DOCTYPE html>
<html lang="de">
<head>
<meta charset="utf-8">
<title>KVR Sensors – Durchflussmesser und Drucksensoren</title>
<link href="https://fonts.googleapis.com/css2?family=Inter:wght@400;500;600;700&display=swap" rel="stylesheet">
<style>
:root{
  --blue:#0a4ea2;
  --orange:#d15c04;
  --grey:#eeeeee;
  --white:#ffffff;
}
*{margin:0;padding:0;box-sizing:border-box}
html,body{width:1200px;height:3481px;overflow:hidden;background:var(--white)}
body{font-family:"Inter",Arial,sans-serif;color:var(--blue);position:relative}
.abs{position:absolute}
a{color:inherit;text-decoration:none}

.topbar{left:0;top:0;width:1200px;height:30px;background:var(--grey)}
.topbar .search{left:715px;top:8px;width:243px;height:15px;background:var(--white)}
.topbar .search svg{position:absolute;right:6px;top:3px}
.topbar .link{top:9px;font-size:10px;color:var(--blue)}

.brand{font-weight:700;font-size:38px;letter-spacing:-1px;color:var(--blue);line-height:1}
.brand-sub{font-size:15px;font-weight:500;color:var(--blue);line-height:1}
.nav a{position:absolute;top:71px;font-size:10.5px;color:var(--blue)}
.nav a.active{font-weight:700}

.hero-visual{left:440px;top:135px;width:760px;height:395px;
  background:radial-gradient(ellipse at 45% 45%,#b9bcc0 0%,#dfe1e3 30%,#f4f5f6 60%,#ffffff 85%)}
.hero-title{left:93px;top:186px;font-size:37px;line-height:38px;font-weight:700;color:var(--blue)}
.hero-lead{left:95px;top:318px;font-size:17px;line-height:23px;color:var(--blue)}
.btn{display:flex;align-items:center;justify-content:center;color:var(--white);background:var(--orange)}
.hero-btn{left:93px;top:390px;width:222px;height:39px;font-size:18px}

.about-photo{left:93px;top:601px;width:500px;height:310px;background:linear-gradient(180deg,#8fb0d6 0%,#c9d9ea 50%,#9aa682 75%,#8a8f7a 100%)}
.h2{font-size:27px;font-weight:600;line-height:32px;color:var(--blue)}
.rule{height:4px;background:var(--orange)}
.about-text{left:690px;top:741px;width:320px;font-size:14.5px;line-height:20.3px}

.prod-img{width:243px;height:207px;background:radial-gradient(circle at 50% 55%,#c7c9cc 0%,#e6e7e8 45%,#eeeeee 100%)}
.card-title{font-size:18px;font-weight:600}
.small{font-size:11.5px;line-height:17.5px}
.prod-btn{width:151px;height:34px;font-size:11.5px}

.adv-title{font-size:17px;font-weight:600}

.apps{left:0;top:1781px;width:1200px;height:494px;background:var(--grey)}
.app-card{top:1958px;width:243px;height:259px;background:var(--white)}
.app-card h3{position:absolute;left:28px;bottom:150px;font-size:17.5px;line-height:23px;font-weight:600}
.app-card .rule{position:absolute;left:28px;top:127px;width:72px;height:3px}
.app-card p{position:absolute;left:28px;top:146px;width:190px}

.cta-band{left:0;top:2399px;width:1200px;height:179px;background:var(--blue)}
.cta-title{left:93px;top:2440px;font-size:27px;line-height:32px;font-weight:600;color:var(--white)}
.cta-lead{left:95px;top:2514px;font-size:17.5px;color:var(--white)}
.cta-btn{left:885px;top:2470px;width:221px;height:39px;font-size:18px}

.news-card{top:2810px;width:243px;height:328px;border:1px solid #ececec;background:var(--white)}
.news-card h3{position:absolute;left:19px;bottom:198px;width:205px;font-size:17.5px;line-height:23px;font-weight:600}
.news-card p{position:absolute;left:19px;top:162px;width:205px}
.news-card .more{position:absolute;left:19px;top:294px;font-size:12.5px;color:var(--orange);display:flex;align-items:center;gap:12px}

.footer-band{left:0;top:3291px;width:1200px;height:190px;background:var(--blue)}
.footer-rule{top:3336px;width:40px;height:3px;background:var(--orange)}
.footer-list{top:3354px;font-size:11px;color:var(--white);line-height:25px}
.footer-search{left:862px;top:3336px;width:243px;height:15px;background:var(--white)}
.footer-search .go{position:absolute;right:0;top:0;width:26px;height:15px;background:var(--orange)}
.social{left:862px;top:3380px;width:18px;height:18px;background:var(--white)}
</style>
</head>
<body>

<header>
  <div class="abs topbar">
    <div class="abs search"><svg width="8" height="8" viewBox="0 0 8 8"><circle cx="3.3" cy="3.3" r="2.5" fill="none" stroke="#0a4ea2" stroke-width="1"/><line x1="5.2" y1="5.2" x2="7.5" y2="7.5" stroke="#0a4ea2"/></svg></div>
    <a class="abs link" style="left:997px">Shop</a>
    <a class="abs link" style="left:1060px">Log in</a>
  </div>
  <div class="abs brand" style="left:93px;top:58px">KVR</div>
  <div class="abs brand-sub" style="left:94px;top:92px">Sensors</div>
  <nav class="nav">
    <a style="left:328px">Pressure sensors</a>
    <a class="active" style="left:459px">Flow meter</a>
    <a style="left:561px">Calibration service</a>
    <a style="left:700px">Special Solutions</a>
    <a style="left:831px">About Us</a>
    <a style="left:923px">Contact Us</a>
    <a style="left:1052px">De <span style="color:#999">|</span> <b>En</b></a>
  </nav>
</header>

<section>
  <div class="abs hero-visual" role="img" aria-label="Produktfoto: Drucksensoren aus Edelstahl mit Kabel auf weißem Hintergrund"></div>
  <h1 class="abs hero-title">Hochpräzise<br>Durchflussmesser<br>und Drucksensoren</h1>
  <p class="abs hero-lead">Präzision, Qualität und zuverlässige<br>Messtechnik – Made in Germany</p>
  <a class="abs btn hero-btn">Kontakt aufnehmen</a>
</section>

<section>
  <div class="abs about-photo" role="img" aria-label="Firmengebäude mit Fahnen unter blauem Himmel"></div>
  <h2 class="abs h2" style="left:690px;top:633px">Kurzvorstellung<br>KVR Sensors</h2>
  <div class="abs rule" style="left:690px;top:714px;width:78px"></div>
  <p class="abs about-text">KVR Sensors ist ein deutscher Hersteller von hochpräzisen Durchflussmessern und Drucksensoren für industrielle Anwendungen. Unsere Messtechnik wird weltweit in Prüfständen, im Automotive-Testing, im Maschinenbau sowie in der Energie- und Prozessindustrie eingesetzt.</p>
</section>

<section>
  <h2 class="abs h2" style="left:93px;top:994px">Hauptproduktbereiche</h2>
  <div class="abs prod-img" style="left:93px;top:1109px" role="img" aria-label="Produktfoto Drucksensor mit Stecker"></div>
  <div class="abs card-title" style="left:350px;top:1137px">Drucksensoren</div>
  <p class="abs small" style="left:350px;top:1170px;width:220px">Zuverlässige Drucksensoren für präzise Messungen unter verschiedensten Einsatzbedingungen</p>
  <a class="abs btn prod-btn" style="left:350px;top:1258px">Produkte entdecken</a>

  <div class="abs prod-img" style="left:607px;top:1109px" role="img" aria-label="Produktfoto Durchflussmesser mit Kabel"></div>
  <div class="abs card-title" style="left:862px;top:1137px">Durchflussmesser</div>
  <p class="abs small" style="left:862px;top:1170px;width:235px">Hochpräzise Durchflussmesslösungen für anspruchsvolle industrielle und technische Anwendungen</p>
  <a class="abs btn prod-btn" style="left:862px;top:1258px;background:var(--blue)">Produkte entdecken</a>
</section>

<section>
  <h2 class="abs h2" style="left:93px;top:1405px">Kernvorteile</h2>
  <svg class="abs" style="left:103px;top:1534px" width="30" height="30" viewBox="0 0 30 30" fill="none" stroke="#d15c04" stroke-width="1.5"><circle cx="11" cy="10" r="4"/><path d="M14 8l12-4M15 12l9 4M9 14l-3 13h12M26 2v6"/></svg>
  <svg class="abs" style="left:350px;top:1534px" width="30" height="30" viewBox="0 0 30 30" fill="none" stroke="#d15c04" stroke-width="1.5"><circle cx="14" cy="11" r="9"/><path d="M10 11l3 3 5-6M8 18l-4 8 5-1 2 4 3-8M20 18l4 8-5-1-2 4-3-8"/></svg>
  <svg class="abs" style="left:607px;top:1534px" width="30" height="30" viewBox="0 0 30 30" fill="none" stroke="#d15c04" stroke-width="1.5"><path d="M5 3v24M15 3v24M25 3v24"/><circle cx="5" cy="18" r="3" fill="#fff"/><circle cx="15" cy="9" r="3" fill="#fff"/><circle cx="25" cy="15" r="3" fill="#fff"/></svg>
  <svg class="abs" style="left:862px;top:1534px" width="30" height="30" viewBox="0 0 30 30" fill="none" stroke="#d15c04" stroke-width="1.5"><path d="M15 24s-8-7-8-13a8 8 0 0116 0c0 6-8 13-8 13z"/><circle cx="15" cy="11" r="3"/><path d="M8 21H3l-1 6h26l-1-6h-5"/></svg>

  <div class="abs adv-title" style="left:93px;top:1590px">Präzision</div>
  <p class="abs small" style="left:93px;top:1626px;width:245px;font-size:11px">Unsere Sensoren bieten höchste Genauigkeit für zuverlässige Messergebnisse in anspruchsvollen Umgebungen, minimieren Fehlerquellen und optimieren Prozesse.</p>
  <div class="abs adv-title" style="left:350px;top:1590px">Qualität</div>
  <p class="abs small" style="left:350px;top:1626px;width:240px;font-size:11px">Hergestellt aus robusten Materialien mit strengen Qualitätskontrollen, gewährleisten unsere Produkte Langlebigkeit und Konsistenz in industriellen Anwendungen.</p>
  <div class="abs adv-title" style="left:607px;top:1590px">Kalibrierung</div>
  <p class="abs small" style="left:607px;top:1626px;width:245px;font-size:11px">Individuelle Kalibrierung nach internationalen Standards sorgt für präzise Anpassung an spezifische Bedürfnisse und langfristige Messstabilität.</p>
  <div class="abs adv-title" style="left:862px;top:1590px">Made in Germany</div>
  <p class="abs small" style="left:862px;top:1626px;width:250px;font-size:11px">Entwickelt und produziert in Deutschland, stehen unsere Produkte für Ingenieurskunst, Innovation und höchste Fertigungsstandards.</p>
</section>

<section>
  <div class="abs apps"></div>
  <h2 class="abs h2" style="left:93px;top:1850px">Anwendungsbereiche</h2>
  <div class="abs app-card" style="left:93px"><h3>Automotive Testing</h3><div class="rule"></div><p class="small">In der Automobilindustrie für präzise Tests von Motoren, Kraftstoffen und Systemen, um Leistung und Sicherheit zu optimieren.</p></div>
  <div class="abs app-card" style="left:350px"><h3>Prüfstände</h3><div class="rule"></div><p class="small">Einsatz in Testständen für genaue Durchfluss- und Druckmessungen, ideal für Forschungs- und Entwicklungszwecke in der Technik.</p></div>
  <div class="abs app-card" style="left:607px"><h3>Maschinenbau</h3><div class="rule"></div><p class="small">Unterstützung im Maschinenbau durch zuverlässige Sensorik für Prozessüberwachung, Wartung und Effizienzsteigerung.</p></div>
  <div class="abs app-card" style="left:862px"><h3>Energie- und<br>Prozessindustrie</h3><div class="rule"></div><p class="small">Für die Überwachung von Flüssigkeiten und Gasen in Energieanlagen und Prozessen, um Effizienz, Sicherheit und Umweltschutz zu gewährleisten.</p></div>
</section>

<section>
  <div class="abs cta-band"></div>
  <h2 class="abs cta-title">Sie benötigen Unterstützung bei der<br>Auswahl der passenden Messtechnik?</h2>
  <p class="abs cta-lead">Unsere Experten beraten Sie gerne.</p>
  <a class="abs btn cta-btn">Kontakt aufnehmen</a>
</section>

<section>
  <h2 class="abs h2" style="left:93px;top:2664px">Aktuelle News und Referenzen<br>aus der Messtechnik</h2>
  <article class="abs news-card" style="left:93px"><h3>Neuer Durchflussmesser für Automotive-Testing</h3><p class="small">Unser neuestes Modell ermöglicht präzise Messungen in Echtzeit für Motorentests, reduziert Kalibrierungszeiten und steigert die Effizienz in der Automobilindustrie.</p><a class="more">Mehr erfahren <svg width="10" height="10" viewBox="0 0 10 10" fill="none" stroke="#d15c04" stroke-width="1.3"><path d="M1 5h8M5.5 1.5L9 5 5.5 8.5"/></svg></a></article>
  <article class="abs news-card" style="left:350px"><h3>Erfolgreiches Projekt in der Energiebranche</h3><p class="small">In Kooperation mit einem führenden Energieanbieter haben wir Drucksensoren für Prozessüberwachung implementiert, die Zuverlässigkeit und Sicherheit in Gasanlagen verbessern.</p><a class="more">Mehr erfahren <svg width="10" height="10" viewBox="0 0 10 10" fill="none" stroke="#d15c04" stroke-width="1.3"><path d="M1 5h8M5.5 1.5L9 5 5.5 8.5"/></svg></a></article>
  <article class="abs news-card" style="left:607px"><h3>Innovation in der Messtechnik</h3><p class="small">Entdecken Sie unsere kalibrierten Sensoren für anspruchsvolle Prüfstände, die höchste Genauigkeit unter extremen Bedingungen bieten und in der Forschung eingesetzt werden.</p><a class="more">Mehr erfahren <svg width="10" height="10" viewBox="0 0 10 10" fill="none" stroke="#d15c04" stroke-width="1.3"><path d="M1 5h8M5.5 1.5L9 5 5.5 8.5"/></svg></a></article>
  <article class="abs news-card" style="left:862px"><h3>Referenz aus dem Maschinenbau</h3><p class="small">Ein Maschinenhersteller berichtet von langlebigen Durchflusslösungen, die Prozesse optimieren und Ausfallzeiten minimieren – Made in Germany für industrielle Anwendungen.</p><a class="more">Mehr erfahren <svg width="10" height="10" viewBox="0 0 10 10" fill="none" stroke="#d15c04" stroke-width="1.3"><path d="M1 5h8M5.5 1.5L9 5 5.5 8.5"/></svg></a></article>
</section>

<footer>
  <div class="abs footer-band"></div>
  <div class="abs brand" style="left:93px;top:3336px;color:#fff;font-size:32px">KVR</div>
  <div class="abs brand-sub" style="left:94px;top:3368px;color:#fff;font-size:13px">Sensors</div>

  <div class="abs footer-rule" style="left:350px"></div>
  <div class="abs footer-list" style="left:350px">+49 301 555 480-0<br>+49 301 555 480-20<br>info@kvr-sensors.example</div>
  <div class="abs footer-rule" style="left:520px"></div>
  <div class="abs footer-list" style="left:520px">Withdrawal policy<br>Privacy Policy<br>Legal Information</div>
  <div class="abs footer-rule" style="left:692px"></div>
  <div class="abs footer-list" style="left:692px">Gender Notice<br>Downloads<br>Contact Us</div>

  <div class="abs footer-search"><div class="go"></div></div>
  <div class="abs social"></div>
</footer>
</body>
</html>
```